依頼詳細
PCとスマホデザインの両方納品をいただきますが、
まずはデザインイメージが確認しやすいPCページのみの提案をお願いします。
スマホページは当選者に納品時にお願いしたいと思います。
スマホサイズについて、表示は横幅375pxで作成し、
デザインデータは2倍の横幅750pxのカンバスサイズで作成してください。
(Retinaディスプレイに対応するため)
レスポンシブウェブデザインを意識したデザインでお願いします。

■サイトマップ
添付の画面遷移図をご確認ください。

■参考サイト
https://www.kurumi-p.co.jp/
https://www.m-sorano.co.jp/
https://www.fujino-printing.co.jp/

■内容について
印刷会社のサイトリニューアルになります。
既存サイト
https://www.hinata-printing.co.jp/

■素材写真
画像データについては、フリー素材から流用して
イメージ画像に当て込んでください。
足りない場合は、一旦他のサイトの写真をサンプルとして
入れてください。(サンプルなどの表記をお願いします)
また、購入が必要な写真などを利用した場合、
価格とサイト名を教えてください。

また、Pixmora Stockで定期契約をしていますので、
Pixmora Stockの画像は使用できます。
デザイン時はカンプ画像をお入れいただきますようお願いします。

※採用サイト寄りのサイトにしたいので、使用する画像は
なるべく人物が入っているものを使用してください。

■ワイヤーフレーム
https://mock.plavetta.jp/view/51830427-216b-4c73-9a05-87162534907e-4182/?fullscreen
コンテンツの構成としてワイヤーフレームを作成しましたが
必ずしもワイヤーフレームの通りではなくて大丈夫です。
TOPページに配置するコンテンツを見ていただき、デザインは
デザイナーの皆様におまかせしたいと思います。

----------------------------------------------------------------------------
【制作物に対するお願い】

■フォントについて
・無料で使えるフォントで作成をお願いします。
・OSに紐づくフォントの使用は控えていただければと思います (ヒラギノなど)

ページ数
1ページ
希望イメージ
シンプル 複雑
単色 カラフル
暗い 明るい
日常 高級
遊び心 厳粛
未来的 伝統的
女性的 男性的
希望する色
青系、既存サイトに載っているロゴのイメージでお願いします。
納品ファイル
• 高解像度JPG (.jpg)
• イラストレーター形式 (.ai)
• フォトショップ形式 (.psd)
補足説明
上記のいずれか1つ(アウトラインありとなしの2つ)と高解像度JPGを納品お願いします。
adobe XDでの納品も可能です。

```html
<!DOCTYPE html>
<html lang="ja">
<head>
<meta charset="utf-8">
<title>ヒナタ印刷 | お客様に最適な印刷メディアを</title>
<link rel="stylesheet" href="https://fonts.googleapis.com/css2?family=Noto+Sans+JP:wght@400;500;700;900&family=Montserrat:wght@500;700;800&display=swap">
<style>
:root{
  --blue:#1b95d3;
  --blue-light:#a9d6ef;
  --ink:#222;
  --text:#444;
  --muted:#888;
  --line:#dcdcdc;
  --gray-bg:#efefef;
  --black:#111;
  --white:#fff;
  --cyan:#00a0e9;
  --magenta:#e4007f;
  --yellow:#f5e24a;
  --key:#1a1a1a;
}
*{margin:0;padding:0;box-sizing:border-box}
html,body{width:1200px;height:3636px;overflow:hidden}
body{position:relative;font-family:"Noto Sans JP",sans-serif;color:var(--text);background:var(--white)}
.en{font-family:"Montserrat",sans-serif}
section,header,footer{position:absolute;left:0;width:1200px}
.ph{position:absolute}

/* header + hero */
.hero{top:0;height:700px;overflow:hidden}
.hero .ph{inset:0;background:linear-gradient(120deg,#e9eaec 0%,#c8ccd2 45%,#8f96a0 100%)}
.hero .shade{position:absolute;inset:0;background:linear-gradient(180deg,rgba(0,0,0,.05),rgba(0,0,0,.25))}
.logo{position:absolute;display:flex;align-items:center;gap:12px;color:var(--white)}
.logo .mark{width:34px;height:34px;background:var(--blue)}
.logo .name{font-weight:900;font-size:26px;letter-spacing:.06em}
.hero .logo{left:40px;top:28px}
.gnav{position:absolute;right:40px;top:36px;display:flex;gap:44px;list-style:none}
.gnav li{color:var(--white);font-size:15px;font-weight:500;letter-spacing:.05em}
.hero-copy{position:absolute;left:0;right:0;top:372px;text-align:center;color:var(--white);text-shadow:0 2px 8px rgba(0,0,0,.35)}
.hero-copy h1{font-size:40px;font-weight:700;letter-spacing:.08em}
.hero-copy p{margin-top:16px;font-size:17px;letter-spacing:.1em}

/* intro */
.intro{top:700px;height:500px;background:var(--white)}
.splash{position:absolute;top:20px;height:460px;width:290px}
.splash.left{left:0;background:linear-gradient(160deg,var(--key) 0%,var(--cyan) 40%,var(--magenta) 70%,var(--yellow) 100%)}
.splash.right{right:0;background:linear-gradient(200deg,var(--cyan) 0%,var(--magenta) 40%,var(--key) 70%,var(--yellow) 100%)}
.intro-body{position:absolute;left:300px;width:600px;top:72px;text-align:center}
.intro-body h2{font-size:30px;font-weight:700;color:var(--ink);letter-spacing:.04em}
.intro-body p{margin-top:28px;font-size:14px;line-height:2.1}

/* business */
.business{top:1200px;height:340px;overflow:hidden}
.business .ph{inset:0;background:linear-gradient(90deg,#3a3f46 0%,#6c7178 45%,#c9b9a2 75%,#e6c870 100%)}
.business .veil{position:absolute;inset:0;background:linear-gradient(90deg,rgba(0,0,0,.55) 0,rgba(0,0,0,.1) 60%)}
.ghost{position:absolute;font-family:"Montserrat",sans-serif;font-weight:800;letter-spacing:.02em;line-height:1}
.business .ghost{left:108px;top:40px;font-size:80px;color:rgba(255,255,255,.18)}
.business h2{position:absolute;left:108px;top:96px;font-size:30px;font-weight:700;color:var(--white)}
.business p{position:absolute;left:108px;top:152px;width:380px;font-size:13px;line-height:1.9;color:var(--white)}
.btn{position:absolute;display:flex;align-items:center;justify-content:space-between;width:220px;height:42px;padding:0 22px;background:var(--blue);color:var(--white);font-size:14px;border-radius:21px}
.btn svg{width:14px;height:14px}
.business .btn{left:108px;top:252px}

/* case */
.case{top:1540px;height:620px}
.case .ghost{left:108px;top:44px;font-size:92px;color:var(--blue-light)}
.sec-title{position:absolute;left:120px;font-size:30px;font-weight:700;color:var(--ink)}
.case .sec-title{top:104px}
.case .btn{right:120px;top:92px}
.cards{position:absolute;left:120px;top:190px;display:flex;gap:30px}
.card{width:300px}
.card .thumb{position:relative;height:210px}
.card h3{margin-top:18px;font-size:16px;font-weight:700;color:var(--ink)}
.card p{margin-top:10px;font-size:13px;line-height:1.8}

/* company / about */
.banners{top:2192px;height:268px;display:flex}
.banner{position:relative;width:600px;height:268px;overflow:hidden}
.banner .ph{inset:0}
.banner.company .ph{background:linear-gradient(135deg,#0d2a5a,#2a5ba8 55%,#111)}
.banner.about .ph{background:linear-gradient(120deg,#111 0%,#111 35%,#00a0e9 55%,#e4007f 75%,#fff100 100%)}
.banner .ghost{right:60px;top:96px;font-size:60px;color:rgba(255,255,255,.22)}
.banner h2{position:absolute;right:80px;top:124px;font-size:28px;font-weight:700;color:var(--white)}

/* news */
.news{top:2460px;height:460px}
.news .ghost{left:108px;top:44px;font-size:92px;color:var(--blue-light)}
.news .sec-title{top:104px}
.news .btn{left:120px;top:208px}
.news-list{position:absolute;left:472px;top:60px;width:608px;list-style:none}
.news-list li{display:flex;align-items:center;gap:40px;height:100px;border-bottom:1px solid var(--line)}
.news-date{width:60px;text-align:center;color:var(--ink)}
.news-date small{display:block;font-size:10px;color:var(--muted)}
.news-date b{display:block;font-size:34px;font-weight:500;line-height:1.1}
.news-list span{font-size:14px}

/* blog */
.blog{top:2920px;height:452px;background:var(--gray-bg)}
.blog .ghost{left:108px;top:40px;font-size:92px;color:var(--white)}
.blog .sec-title{top:100px}
.blog .btn{left:120px;top:196px}
.posts{position:absolute;left:448px;top:60px;display:flex;gap:16px}
.post{width:236px}
.post .thumb{position:relative;height:176px;background:linear-gradient(135deg,#c9ccd3,#8e949d)}
.post h3{margin-top:14px;font-size:13px;font-weight:500;color:var(--ink)}
.post time{display:block;margin-top:6px;font-size:11px;color:var(--muted)}

/* footer */
.footer{top:3372px;height:264px;background:var(--black);color:#ccc}
.footer .logo{left:120px;top:60px}
.address{position:absolute;left:680px;top:56px;font-size:13px;line-height:1.9;font-style:normal}
.fnav{position:absolute;left:120px;top:150px;display:flex;gap:16px;list-style:none;font-size:12px}
.fnav li+li::before{content:"|";margin-right:16px;color:#666}
.copy{position:absolute;left:0;right:0;bottom:24px;text-align:center;font-size:11px;color:#888}
</style>
</head>
<body>

<header class="hero">
  <div class="ph" role="img" aria-label="タブレットを操作する手と色見本のあるオフィスのデスク写真"></div>
  <div class="shade"></div>
  <div class="logo"><span class="mark"></span><span class="name">ヒナタ印刷</span></div>
  <ul class="gnav">
    <li>業務案内</li><li>入稿について</li><li>事例紹介</li><li>会社概要</li>
  </ul>
  <div class="hero-copy">
    <h1>お客様に最適な印刷メディアを</h1>
    <p>―― 紙からページ制作まで、印刷のことならお任せください ――</p>
  </div>
</header>

<section class="intro">
  <div class="splash left" role="img" aria-label="シアン・マゼンタ・イエロー・ブラックのインクが飛び散る写真"></div>
  <div class="splash right" role="img" aria-label="シアン・マゼンタ・イエロー・ブラックのインクが飛び散る写真"></div>
  <div class="intro-body">
    <h2>ヒナタ印刷はお客様と共に考えます。</h2>
    <p>当社は創業以来、地域の皆様と共に歩んでまいりました。<br>チラシ、パンフレット、冊子など、様々な印刷物を<br>一つひとつ丁寧に、心を込めてお届けしています。</p>
    <p>しかし情報の伝え方は時代とともに変わり続けています。<br>お客様の想いを正しく届けるために、私たちは<br>企画から仕上げまで寄り添い、共に考え続けます。</p>
    <p>お客様の「伝えたい」を大切に、これからも<br>新しい価値を生み出す印刷会社であり続けます。</p>
  </div>
</section>

<section class="business">
  <div class="ph" role="img" aria-label="色見本を広げて打ち合わせをする人の手元写真"></div>
  <div class="veil"></div>
  <div class="ghost">BUSINESS</div>
  <h2>業務案内</h2>
  <p>ヒナタ印刷は、企画・デザインから印刷・製本まで、<br>お客様のニーズに合わせた最適なご提案をいたします。<br>小ロットから大量印刷まで幅広く対応可能です。</p>
  <div class="btn">詳しく見る<svg viewBox="0 0 14 14"><path d="M4 2l6 5-6 5" fill="none" stroke="#fff" stroke-width="2"/></svg></div>
</section>

<section class="case">
  <div class="ghost">CASE</div>
  <h2 class="sec-title">事例紹介</h2>
  <div class="btn">一覧を見る<svg viewBox="0 0 14 14"><path d="M4 2l6 5-6 5" fill="none" stroke="#fff" stroke-width="2"/></svg></div>
  <div class="cards">
    <article class="card">
      <div class="thumb ph" role="img" aria-label="制作したパッケージや印刷物の写真" style="background:linear-gradient(135deg,#e6e0d4,#a8b7c4)"></div>
      <h3>株式会社会社名</h3>
      <p>テキストが入ります。テキストが入ります。テキストが入ります。</p>
    </article>
    <article class="card">
      <div class="thumb ph" role="img" aria-label="制作したカタログや冊子の写真" style="background:linear-gradient(135deg,#d9514e,#e9d3b0)"></div>
      <h3>株式会社会社名</h3>
      <p>テキストが入ります。テキストが入ります。テキストが入ります。</p>
    </article>
    <article class="card">
      <div class="thumb ph" role="img" aria-label="制作したパンフレットの写真" style="background:linear-gradient(135deg,#c7d8e6,#8aa6b8)"></div>
      <h3>株式会社会社名</h3>
      <p>テキストが入ります。テキストが入ります。テキストが入ります。</p>
    </article>
  </div>
</section>

<section class="banners">
  <div class="banner company">
    <div class="ph" role="img" aria-label="会社の看板がある社屋の写真"></div>
    <div class="ghost">COMPANY</div>
    <h2>会社概要</h2>
  </div>
  <div class="banner about">
    <div class="ph" role="img" aria-label="カラフルなインクが広がるイメージ写真"></div>
    <div class="ghost">ABOUT</div>
    <h2>入稿について</h2>
  </div>
</section>

<section class="news">
  <div class="ghost">NEWS</div>
  <h2 class="sec-title">新着情報</h2>
  <div class="btn">一覧を見る<svg viewBox="0 0 14 14"><path d="M4 2l6 5-6 5" fill="none" stroke="#fff" stroke-width="2"/></svg></div>
  <ul class="news-list">
    <li><div class="news-date en"><small>2020.05</small><b>09</b></div><span>テキストが入ります。テキストが入ります。テキストが入ります。</span></li>
    <li><div class="news-date en"><small>2020.05</small><b>01</b></div><span>テキストが入ります。テキストが入ります。テキストが入ります。</span></li>
    <li><div class="news-date en"><small>2020.04</small><b>07</b></div><span>テキストが入ります。テキストが入ります。テキストが入ります。</span></li>
  </ul>
</section>

<section class="blog">
  <div class="ghost">BLOG</div>
  <h2 class="sec-title">ブログ</h2>
  <div class="btn">一覧を見る<svg viewBox="0 0 14 14"><path d="M4 2l6 5-6 5" fill="none" stroke="#fff" stroke-width="2"/></svg></div>
  <div class="posts">
    <article class="post"><div class="thumb" role="img" aria-label="社内表彰式の様子の写真"></div><h3>社員表彰を行いました</h3><time class="en">2020.05.08</time></article>
    <article class="post"><div class="thumb" role="img" aria-label="社内研修会の会場の写真"></div><h3>社内研修会を開催しました</h3><time class="en">2020.04.24</time></article>
    <article class="post"><div class="thumb" role="img" aria-label="セミナー会場の様子の写真"></div><h3>セミナーに参加しました</h3><time class="en">2020.04.10</time></article>
  </div>
</section>

<footer class="footer">
  <div class="logo"><span class="mark"></span><span class="name">ヒナタ印刷</span></div>
  <address class="address">〒000-0000 架空県ひなた市中央1丁目2番3号<br>TEL：000-000-0000<br>FAX：000-000-0001</address>
  <ul class="fnav"><li>お問い合わせ</li><li>プライバシーポリシー</li><li>サイトマップ</li></ul>
  <p class="copy">Copyright © 株式会社ヒナタ印刷</p>
</footer>

</body>
</html>
```